Building Maintenance Flyer specialising in hot and silent pressure cleaning

Hi. I love this flyer. I would like something similar but with hot water pressure washing and building maintenance

Ferro Lane & Services provides high pressure steam cleaning and water blasting services throughout Brisbane and surrounding areas, covering the Industrial, Commercial, Strata and Residential property owners sectors.

FLS combining the cleaning power of heat with state-of-the-art silent equipment, accredited technicians and a steadfast commitment to the environment. We offer the best Prompt, Professional Service.

Fully Accredited & Certified Technicians
100% Satisfaction Guaranteed
We are a family owned and operated business and love what we do. No job is too big or too small and we take pride in our work.
All of our services are undertaken using industry leading equipment and, providing safe and superior results.

Our business is covered by 20 million full public liability insurance and we operate within strict health & safety guidelines, providing all our clients with complete peace of mind. Project plans and risk assessments can also be provided upon request.

BODY CORPORATES

BUILDING FAÇADE CLEANING

CAR PARKS – underground, single and multi level

DRIVE THRU

FOOD PRODUCTION FACILITIES CLEANING SANITISING

SHOPPING CENTRES

BIRD MANAGEMENT AND DECONTAMINATION

GENERAL MAINTENANCE

CONSTRUCTION CLEAN UPS

SPILL MANAGEMENT

CONCRETE CLEANING AND DEGRASING

CONCRETE SEALING

FACTORY CLEANING & CLEAN UP

ENVIRONMENTAL DECONTAMINATION OF HEAVY VEHICLES AND EQUIPMENT

SITE CLEANS AND RUBBISH REMOVAL

MANUFACTURING PLANTS

Target Market(s)

Facility Managers, Commercial and Industrial Property Owners, Property Managers, Schools, Restaurants,

Industry/Entity Type

Pressure Cleaning

Font styles to use
Sans Serif

Colors
0293ce
00a990
33a6d7
33b8a4

Requirements
Must have
• SILENT HOT WATER PRESSURE CLEANING
Runs up to 120 Degrees Celsius
SANITISING - Bin areas, outdoor areas, cafe's, restaurants, schools, drive thru's
Blue's and Greens to link in with our logo

```html
<!DOCTYPE html>
<html lang="en">
<head>
<meta charset="utf-8">
<title>FLS Pressure Cleaning Flyer</title>
<link href="https://fonts.googleapis.com/css2?family=Poppins:wght@400;500;600;700;800&display=swap" rel="stylesheet">
<style>
:root{
  --blue:#0293ce;
  --blue-deep:#1662ad;
  --teal:#00a990;
  --sky:#33a6d7;
  --mint:#33b8a4;
  --ink:#2a2f36;
  --stage:#4a1414;
  --paper:#ffffff;
}
*{box-sizing:border-box;margin:0;padding:0}
html,body{width:1200px;height:866px;overflow:hidden}
body{background:var(--stage);font-family:'Poppins',sans-serif;position:relative;color:var(--ink)}
.sheet{position:absolute;top:79px;width:490px;height:692px;background:var(--paper);overflow:hidden}
.sheet--front{left:89px;background:linear-gradient(180deg,#fff 0%,#f1f3f5 100%)}
.sheet--back{left:622px}
.side-label{position:absolute;top:796px;width:490px;text-align:center;color:#fff;font-weight:600;font-size:16px;letter-spacing:1px}

/* front */
.hero-photo{position:absolute;left:0;top:0;width:400px;height:224px;background:radial-gradient(ellipse at 45% 55%,#5a5f66 0%,#9ea4aa 45%,#f4f5f6 80%)}
.brand{position:absolute;left:318px;top:52px;display:flex;align-items:center;gap:10px}
.brand__dot{width:34px;height:34px;border-radius:50%;background:var(--blue)}
.brand__name{font-weight:800;font-size:38px;color:var(--blue-deep);line-height:1}
.band{position:absolute;left:0;top:223px;width:490px;height:64px;background:linear-gradient(90deg,var(--mint) 0%,var(--sky) 45%,var(--blue-deep) 100%);color:#fff;padding:9px 0 0 21px}
.band__title{font-weight:800;font-size:28.5px;line-height:1.05;letter-spacing:.2px}
.band__sub{font-size:14px;line-height:1.5}
.features{position:absolute;left:0;top:307px;width:490px;display:flex}
.feature{flex:1;text-align:center;position:relative}
.feature+.feature::before{content:"";position:absolute;left:0;top:2px;width:2px;height:96px;background:var(--blue)}
.feature__badge{width:78px;height:78px;border-radius:50%;margin:0 auto 5px;background:conic-gradient(var(--mint) 0 40%,var(--blue-deep) 40% 100%);padding:5px}
.feature__badge svg{width:68px;height:68px;display:block}
.feature__title{font-weight:600;font-size:11.5px;color:var(--blue-deep);line-height:1.2}
.feature__text{font-size:11.5px;color:var(--blue);line-height:1.2}
.solutions{position:absolute;left:32px;top:462px}
.solutions__heading{font-weight:500;font-size:16px;color:var(--blue-deep);margin-bottom:6px}
.solutions__list{list-style:none}
.solutions__list li{display:flex;align-items:center;gap:12px;font-size:12.6px;height:21px}
.solutions__list li::before{content:"";width:13px;height:13px;border-radius:50%;border:2.5px solid var(--blue)}
.person-photo{position:absolute;left:251px;top:421px;width:239px;height:271px;background:linear-gradient(180deg,#e9ecef 0%,#c9d3dc 30%,#2f6fc0 60%,#1d4f9b 100%);border-top-left-radius:120px 90px}

/* back */
.top-photo{position:absolute;left:0;top:0;width:490px;height:200px;background:linear-gradient(180deg,#6d9fc8 0%,#8fb89a 45%,#cfe0ea 78%,#fff 100%)}
.copy{position:absolute;z-index:2;left:25px;width:440px;font-size:10.8px;line-height:13px;text-align:justify}
.copy--intro{top:185px}
.copy--tech{top:235px}
.copy--cover{top:379px}
.checklist{position:absolute;z-index:2;left:25px;top:292px;width:440px;font-size:10.8px;line-height:13px}
.checklist__heading{font-weight:600;color:var(--blue-deep)}
.checklist ul{list-style:none}
.checklist li::before{content:"";display:inline-block;width:5px;height:5px;border-radius:50%;background:var(--blue-deep);margin-right:4px;vertical-align:1px}
.lower-bg{position:absolute;z-index:1;left:0;top:400px;width:490px;height:292px;background:linear-gradient(170deg,rgba(255,255,255,0) 0%,#eef1f3 30%,#dce3e8 60%,#b9c2c8 100%)}
.worker-photo{position:absolute;z-index:1;left:274px;top:470px;width:216px;height:222px;background:linear-gradient(135deg,#c6ccd0 0%,#d8e34a 35%,#b7c23a 55%,#8e979d 100%);border-top-left-radius:60px}
.seal{position:absolute;z-index:2;left:386px;top:438px;width:78px;height:68px}
.promo{position:absolute;z-index:2;left:26px;top:446px;font-size:14px;line-height:16.5px;color:var(--blue-deep)}
.promo strong{font-weight:600}
.promo span{color:var(--blue)}
.contact{position:absolute;z-index:2;left:26px;top:537px}
.contact__heading{font-weight:700;font-size:24px;color:var(--teal);line-height:1.2;margin-bottom:5px}
.contact__row{display:flex;align-items:center;gap:10px;font-size:16px;line-height:19.5px;color:#1e2228}
.contact__row svg{width:13px;height:13px;fill:var(--blue)}
.social{position:absolute;z-index:2;left:26px;top:645px;display:flex;gap:3px}
.social span{width:17px;height:17px;border-radius:50%;background:var(--blue-deep)}
</style>
</head>
<body>

<section class="sheet sheet--front">
  <div class="hero-photo" role="img" aria-label="Trailer-mounted hot water pressure cleaning unit"></div>
  <div class="brand"><span class="brand__dot"></span><span class="brand__name">FLS</span></div>

  <div class="band">
    <h1 class="band__title">ALL COMMERCIAL &amp; PROPERTY</h1>
    <p class="band__sub">FLS – servicing Southeast’s Commercial &amp; Industrial sector 24/7</p>
  </div>

  <div class="features">
    <div class="feature">
      <div class="feature__badge">
        <svg viewBox="0 0 68 68"><circle cx="34" cy="34" r="34" fill="#e6e8ea"/><circle cx="34" cy="34" r="20" fill="none" stroke="#222" stroke-width="3" stroke-dasharray="5 4"/><text x="34" y="40" text-anchor="middle" font-family="Poppins,sans-serif" font-weight="700" font-size="16" fill="#222">24</text></svg>
      </div>
      <p class="feature__title">WE OPERATE 24/7</p>
      <p class="feature__text">7 days a week</p>
    </div>
    <div class="feature">
      <div class="feature__badge">
        <svg viewBox="0 0 68 68"><circle cx="34" cy="34" r="34" fill="#e6e8ea"/><path d="M22 30a12 12 0 0 1 24 0z" fill="#222"/><rect x="20" y="29" width="28" height="4" rx="2" fill="#222"/><path d="M18 54c2-10 8-14 16-14s14 4 16 14z" fill="#222"/></svg>
      </div>
      <p class="feature__title">SILENT HOT WATER</p>
      <p class="feature__text">pressure cleaning<br>150degrees</p>
    </div>
    <div class="feature">
      <div class="feature__badge">
        <svg viewBox="0 0 68 68"><circle cx="34" cy="34" r="34" fill="#e6e8ea"/><rect x="18" y="32" width="8" height="18" fill="#222"/><path d="M28 32l8-12c3 0 4 2 3 5l-2 6h10c3 0 4 3 3 5l-3 12c-1 2-2 2-4 2H28z" fill="#222"/></svg>
      </div>
      <p class="feature__title">COVID-19</p>
      <p class="feature__text">Trained</p>
    </div>
  </div>

  <div class="solutions">
    <h2 class="solutions__heading">SOLUTIONS FOR:</h2>
    <ul class="solutions__list">
      <li>COVID-19 Infection Control</li>
      <li>Building Management</li>
      <li>Bin Cleaning&amp; Sanitisation</li>
      <li>Garden Maintenance</li>
      <li>Common Area Cleaning</li>
      <li>Bird waste removal</li>
      <li>Mould &amp; Mildew removal</li>
      <li>Oil &amp; Grease elimination</li>
    </ul>
  </div>

  <div class="person-photo" role="img" aria-label="Technician in blue uniform holding a tablet"></div>
</section>
<p class="side-label" style="left:89px">FRONT</p>

<section class="sheet sheet--back">
  <div class="top-photo" role="img" aria-label="Worker using a pressure washer wand outdoors"></div>
  <div class="lower-bg"></div>

  <p class="copy copy--intro">Ferro Lane &amp; Services provides high pressure steam cleaning and water blasting services throughout Brisbane and surrounding areas, covering the Industrial, Commercial, Strata and Residential property owners sectors.</p>
  <p class="copy copy--tech">FLS combining the cleaning power of heat with state-of-the-art silent equipment, accredited technicians and a steadfast commitment to the environment. We offer the best Prompt, Professional Service.</p>

  <div class="checklist">
    <p class="checklist__heading">Fully Accredited &amp; Certified Technicians</p>
    <ul>
      <li>100% Satisfaction Guaranteed</li>
      <li>We are a family owned and operated business and love what we do.</li>
      <li>No job is too big or too small and we take pride in our work.</li>
      <li>All of our services are undertaken using industry leading equipment and,</li>
      <li>providing safe and superior results.</li>
    </ul>
  </div>

  <p class="copy copy--cover">Our business is covered by 20 million full public liability insurance and we operate within strict health &amp; safety guidelines, providing all our clients with complete peace of mind. Project plans and risk assessments can also be provided upon request.</p>

  <div class="worker-photo" role="img" aria-label="Worker in hi-vis rain gear pressure cleaning pavers"></div>
  <svg class="seal" viewBox="0 0 78 68" aria-hidden="true">
    <path d="M4 46h70l-6 8 6 8H4l6-8z" fill="#1b56a6"/>
    <circle cx="39" cy="32" r="30" fill="#1b56a6"/>
    <circle cx="39" cy="32" r="24" fill="none" stroke="#fff" stroke-width="1.5"/>
  </svg>

  <div class="promo">
    <strong>SILENT HOT WATER PRESSURE CLEANING</strong><br>
    <strong>Runs up to 120 Degrees Celsius</strong><br>
    <strong>SANITISING</strong> <span>- Bin areas, outdoor areas</span><br>
    <span>cafe's, restaurants, schools</span><br>
    <span>drive thru's</span>
  </div>

  <div class="contact">
    <h2 class="contact__heading">CONTACT US</h2>
    <p class="contact__row"><svg viewBox="0 0 24 24"><path d="M6.6 10.8a15 15 0 0 0 6.6 6.6l2.2-2.2c.3-.3.7-.4 1-.2 1.1.4 2.3.6 3.6.6.6 0 1 .4 1 1V20c0 .6-.4 1-1 1A17 17 0 0 1 3 4c0-.6.4-1 1-1h3.5c.6 0 1 .4 1 1 0 1.3.2 2.5.6 3.6.1.3 0 .7-.2 1z"/></svg>1-800-555-0142</p>
    <p class="contact__row"><svg viewBox="0 0 24 24"><path d="M2 5h20v14H2zm2 2v.5l8 5 8-5V7z"/></svg>SERVICE@FLSCLEAN.COM</p>
    <p class="contact__row"><svg viewBox="0 0 24 24"><circle cx="12" cy="12" r="10"/></svg>WWW.FLSCLEAN.COM</p>
  </div>
  <div class="social" aria-hidden="true"><span></span><span></span><span></span><span></span><span></span><span></span></div>
</section>
<p class="side-label" style="left:622px">BACK</p>

</body>
</html>
```